Food label for BarBQ sauce and creole seasoning under the name GOLDEN MERCY

I need a label design using the name "GOLDEN MERCY" that will be used on bottles of Bar B Q sauce, both Creole and Cajun, and dry Cajun and dry Creole seasoning. I have attached a copy of the letter style we will be using. It is NOT a religious product or has any religious meaning. It comes from a saying old southerners used when they tasted something special -"Oh Golden Mercy". The labels for the Bar B Q sauces will be 5" wide by 3" tall, and the dry seasonings will be 5" wide by 3 1/2" tall. The products will that they are from South Louisiana and should reflect the typical food from the New Orleans area. This produce name is a REGISTERED TRADE NAME with the US trademark office.

```html
<!DOCTYPE html>
<html lang="en">
<head>
<meta charset="utf-8">
<title>Golden Mercy BBQ Sauce Label</title>
<link rel="stylesheet" href="https://fonts.googleapis.com/css2?family=Nunito:wght@900&family=Rye&family=Russo+One&display=swap">
<style>
  :root {
    --bg: #ffffff;
    --rim-orange: #ff6a00;
    --rim-gold: #ffc400;
    --ink: #000000;
    --grad-orange: #ff7a1a;
    --grad-red: #ff1a00;
    --grad-gold: #ffcc00;
    --band: #fdfc9c;
    --sauce-red: #cc3300;
    --name-red: #e8141a;
    --white: #ffffff;
  }
  html, body {
    margin: 0;
    padding: 0;
    width: 1200px;
    height: 973px;
    overflow: hidden;
    background: var(--bg);
  }
  .label {
    display: block;
    width: 1200px;
    height: 973px;
  }
  .product-type {
    font-family: "Nunito", "Arial Rounded MT Bold", sans-serif;
    font-weight: 900;
    font-size: 132px;
    fill: var(--sauce-red);
    stroke: var(--white);
    stroke-width: 2;
    paint-order: stroke;
  }
  .product-type-shadow {
    font-family: "Nunito", "Arial Rounded MT Bold", sans-serif;
    font-weight: 900;
    font-size: 132px;
    fill: var(--ink);
  }
  .brand-name {
    font-family: "Rye", serif;
    font-size: 140px;
    fill: var(--name-red);
  }
  .brand-name-inline {
    font-family: "Rye", serif;
    font-size: 140px;
    fill: none;
    stroke: var(--white);
    stroke-width: 1.2;
  }
  .flavor {
    font-family: "Russo One", sans-serif;
    font-size: 66px;
    fill: var(--white);
    letter-spacing: 2px;
  }
  .flavor-shadow {
    font-family: "Russo One", sans-serif;
    font-size: 66px;
    fill: var(--ink);
    letter-spacing: 2px;
  }
</style>
</head>
<body>
<svg class="label" viewBox="0 0 1200 973" xmlns="http://www.w3.org/2000/svg" aria-label="Golden Mercy BBQ sauce, Creole">
  <defs>
    <linearGradient id="label-fill" x1="0" y1="0" x2="1" y2="0">
      <stop offset="0" stop-color="var(--grad-orange)"/>
      <stop offset="0.17" stop-color="var(--grad-red)"/>
      <stop offset="0.5" stop-color="var(--grad-gold)"/>
      <stop offset="0.83" stop-color="var(--grad-red)"/>
      <stop offset="1" stop-color="var(--grad-orange)"/>
    </linearGradient>
  </defs>

  <!-- frame rings -->
  <rect class="rim-outer" x="35" y="143" width="1134" height="680" rx="300" fill="var(--rim-orange)"/>
  <rect class="rim-gold" x="48" y="155" width="1108" height="656" rx="290" fill="var(--rim-gold)"/>
  <rect class="rim-inner" x="60" y="165" width="1084" height="636" rx="280" fill="var(--rim-orange)"/>
  <rect class="label-body" x="72" y="174" width="1060" height="618" rx="272" fill="url(#label-fill)" stroke="var(--ink)" stroke-width="7"/>

  <!-- name band -->
  <rect class="name-band" x="82" y="376" width="1040" height="225" rx="14" fill="var(--band)"/>

  <!-- product type -->
  <text class="product-type-shadow" x="301" y="340" textLength="622" lengthAdjust="spacingAndGlyphs">BBQ sauce</text>
  <text class="product-type" x="295" y="333" textLength="622" lengthAdjust="spacingAndGlyphs">BBQ sauce</text>

  <!-- brand name -->
  <text class="brand-name" x="127" y="536" textLength="945" lengthAdjust="spacingAndGlyphs">GOLDEN MERCY</text>
  <text class="brand-name-inline" x="127" y="536" textLength="945" lengthAdjust="spacingAndGlyphs">GOLDEN MERCY</text>

  <!-- flavour -->
  <text class="flavor-shadow" x="439" y="721" textLength="290" lengthAdjust="spacingAndGlyphs">CREOLE</text>
  <text class="flavor" x="435" y="716" textLength="290" lengthAdjust="spacingAndGlyphs">CREOLE</text>
</svg>
</body>
</html>
```